Create a Eye Catching Web Design

We need an informative web design that needs to be eye catching and unique. All of the information needs to be on that page - We have a shopfront setup in the next 2 weeks so the website needs to be ready asap. We are selling mainly rehabilitation aids and mobility products.

The website is main purpose is to inform customers about our range of products, address and phone number. This is an interim website until we get an ecommerce website setup. We are not looking for an ecommerce website, just simple, eye-catching and informative. clean, crisp and modern -target age 45-75 yo (men and women)

I have included our logo and brochure designed with our range of product categories.

The website needs to be designed, coded and setup completely as a finished product.

As soon as the website design is chosen, the chosen designer would need to get the website up and running. If the website design is chosen and great, we could use the same designer for the ecommerce build as well.

www.tolvenacare.com
www.tolvenacare.com.au

Reason: I haven't received as many designs but variations from the same designers.

Target Market(s)

45-75

Industry/Entity Type

Health And Wellness

Coding

Coded - Design and coding required

Number of Pages Required

2 page

Font styles to use
Sans Serif

Requirements
Nice to have
• clean design, modern feel - not cluttered - something unique. for the market age

```html
<!DOCTYPE html>
<html lang="en">
<head>
<meta charset="utf-8">
<title>Contact Us – Tolvena Care</title>
<link href="https://fonts.googleapis.com/css2?family=Oswald:wght@300;400&family=Roboto:wght@400;500;700&display=swap" rel="stylesheet">
<style>
:root{
  --red:#e8202a;
  --ink:#222;
  --text:#555;
  --muted:#8a8a8a;
  --line:#e6e6e6;
  --band:#f4f4f4;
  --footer:#252637;
  --map:#e6e6e6;
}
*{margin:0;padding:0;box-sizing:border-box}
html,body{width:1177px;height:1200px;overflow:hidden;background:#fff}
body{position:relative;font-family:Roboto,Arial,sans-serif;color:var(--text)}
.abs{position:absolute}
a{color:inherit;text-decoration:none}

/* top bar */
.topbar{left:0;top:0;width:1177px;height:37px;border-bottom:1px solid var(--line);font-size:12.5px;color:#666}
.topbar .item{top:0;height:36px;display:flex;align-items:center;gap:6px}
.topbar .sep{top:0;width:1px;height:36px;background:var(--line)}
.topbar .social{top:12px;width:12px;height:12px;border-radius:50%;background:#b5b5b5}

/* header */
.logo{font-family:Roboto,sans-serif;font-weight:700;color:var(--red);letter-spacing:1px;display:flex;align-items:center;gap:6px}
.logo .dot{width:12px;height:12px;border-radius:50%;background:var(--red)}
.nav{top:68px;font-size:13.5px;color:var(--ink)}
.nav.active{color:var(--red)}
.search{left:1059px;top:63px;width:30px;height:30px;border-radius:50%;background:#f2f2f2}

/* title band */
.band{left:0;top:119px;width:1177px;height:108px;background:var(--band)}
.page-title{left:85px;top:151px;font-family:Oswald,sans-serif;font-size:34px;font-weight:400;color:var(--ink);line-height:1}
.crumbs{right:88px;top:165px;font-size:13.5px;color:var(--ink);display:flex;align-items:center;gap:10px}
.crumbs .here{color:var(--red)}

/* contact */
.h2{font-family:Oswald,sans-serif;font-weight:300;font-size:29px;color:var(--ink);line-height:1}
.rule{width:30px;height:2px;background:#ddd}
.info{left:87px;font-size:12.5px;color:#555;display:flex;align-items:center;gap:8px}
.divider{left:403px;top:284px;width:1px;height:196px;background:var(--line)}
.label{font-size:14px;color:var(--ink)}
.ph{font-size:11.5px;color:var(--muted)}
.field-line{height:1px;background:var(--line)}
.send{left:1058px;top:445px;width:30px;height:30px;border-radius:50%;background:var(--red);display:flex;align-items:center;justify-content:center}

/* map */
.map{left:0;top:539px;width:1177px;height:365px;background:linear-gradient(160deg,#ececec,#e2e2e2)}

/* footer */
.footer{left:0;top:904px;width:1177px;height:296px;background:var(--footer);color:#fff}
.footer .logo{color:#fff}
.footer .logo .dot{background:#fff}
.fh{font-size:16px;color:#fff;font-weight:400}
.frule{width:30px;height:2px;background:#4a4b5c}
.ftext{font-size:12.5px;color:#fff;display:flex;align-items:center;gap:8px}
.chev{color:#777;font-size:10px}
.fdot{width:7px;height:7px;border-radius:50%;background:#fff}
.submit{left:865px;top:1079px;width:96px;height:34px;border-radius:17px;background:var(--red);color:#fff;font-size:12.5px;font-weight:700;display:flex;align-items:center;justify-content:center}
.totop{left:1120px;top:1135px;width:34px;height:34px;border-radius:50%;background:#fff;display:flex;align-items:center;justify-content:center}
</style>
</head>
<body>

<!-- top bar -->
<div class="abs topbar">
  <div class="abs item" style="left:86px">
    <svg width="9" height="14" viewBox="0 0 9 14"><rect x="0.5" y="0.5" width="8" height="13" rx="1.5" fill="none" stroke="#aaa"/><rect x="3" y="11" width="3" height="1" fill="#aaa"/></svg>
    Phone :&nbsp; 40517328.
  </div>
  <div class="abs sep" style="left:224px"></div>
  <div class="abs item" style="left:241px">
    <svg width="10" height="13" viewBox="0 0 10 13"><path d="M5 0a5 5 0 0 0-5 5c0 3.5 5 8 5 8s5-4.5 5-8a5 5 0 0 0-5-5z" fill="#aaa"/><circle cx="5" cy="5" r="1.8" fill="#fff"/></svg>
    Address :&nbsp; 52 Ellery st, Parkes.
  </div>
  <div class="abs sep" style="left:465px"></div>
  <div class="abs item" style="left:483px">
    <svg width="12" height="9" viewBox="0 0 12 9"><rect width="12" height="9" fill="#aaa"/><path d="M0 0l6 5 6-5" fill="none" stroke="#fff"/></svg>
    Email :&nbsp; www.tolvenacare.com
  </div>
  <div class="abs sep" style="left:948px"></div>
  <div class="abs social" style="left:960px"></div>
  <div class="abs sep" style="left:983px"></div>
  <div class="abs social" style="left:995px"></div>
  <div class="abs sep" style="left:1018px"></div>
  <div class="abs social" style="left:1029px"></div>
  <div class="abs sep" style="left:1052px"></div>
  <div class="abs social" style="left:1064px"></div>
  <div class="abs sep" style="left:1087px"></div>
</div>

<!-- header -->
<div class="abs logo" style="left:87px;top:64px;font-size:27px">TOLVENA CARE <span class="dot"></span></div>
<svg class="abs" style="left:527px;top:73px" width="12" height="11" viewBox="0 0 12 11"><path d="M6 0L0 5.5h1.6V11h3V7.5h2.8V11h3V5.5H12z" fill="#222"/></svg>
<a class="abs nav" style="left:561px">About Us</a>
<a class="abs nav" style="left:651px">Services</a>
<a class="abs nav" style="left:737px">Products</a>
<a class="abs nav" style="left:827px">Gallery</a>
<a class="abs nav" style="left:902px">Blog</a>
<a class="abs nav active" style="left:965px">Contact Us</a>
<div class="abs search">
  <svg width="30" height="30" viewBox="0 0 30 30"><circle cx="14" cy="14" r="4.5" fill="none" stroke="#888" stroke-width="1.2"/><path d="M17.3 17.3l3.5 3.5" stroke="#888" stroke-width="1.2"/></svg>
</div>

<!-- title band -->
<div class="abs band"></div>
<h1 class="abs page-title">Contact Us</h1>
<div class="abs crumbs">
  <svg width="12" height="11" viewBox="0 0 12 11"><path d="M6 0L0 5.5h1.6V11h3V7.5h2.8V11h3V5.5H12z" fill="#222"/></svg>
  <span>&nbsp;Home</span><span>|</span><span class="here">Contact us</span>
</div>

<!-- contact information -->
<h2 class="abs h2" style="left:87px;top:276px">Contact information</h2>
<div class="abs rule" style="left:89px;top:316px"></div>
<div class="abs info" style="top:344px">
  <svg width="10" height="13" viewBox="0 0 10 13"><path d="M5 0a5 5 0 0 0-5 5c0 3.5 5 8 5 8s5-4.5 5-8a5 5 0 0 0-5-5z" fill="#e8202a"/><circle cx="5" cy="5" r="1.8" fill="#fff"/></svg>
  52 ellery st, Parkes.
</div>
<div class="abs info" style="top:380px">
  <svg width="10" height="10" viewBox="0 0 10 10"><path d="M2 0l2 2.5-1.2 1.3c.8 1.6 1.8 2.6 3.4 3.4L7.5 6 10 8l-1.5 2C4 9.5.5 6 0 1.5z" fill="#e8202a"/></svg>
  Phone: 40517328.
</div>
<div class="abs info" style="top:418px">
  <svg width="11" height="8" viewBox="0 0 11 8"><rect width="11" height="8" fill="#e8202a"/><path d="M0 0l5.5 4.5L11 0" fill="none" stroke="#fff"/></svg>
  Email: www.tolvenacare.com
</div>
<div class="abs divider"></div>

<!-- get in touch -->
<h2 class="abs h2" style="left:520px;top:276px">Get in Touch</h2>
<div class="abs rule" style="left:522px;top:316px"></div>
<label class="abs label" style="left:520px;top:344px">Name:</label>
<span class="abs ph" style="left:521px;top:370px">Enter your name...</span>
<div class="abs field-line" style="left:521px;top:392px;width:274px"></div>
<label class="abs label" style="left:813px;top:344px">Email:</label>
<span class="abs ph" style="left:814px;top:370px">Enter your email...</span>
<div class="abs field-line" style="left:814px;top:392px;width:275px"></div>
<label class="abs label" style="left:520px;top:411px">Message:</label>
<span class="abs ph" style="left:521px;top:436px">Enter your message...</span>
<div class="abs field-line" style="left:521px;top:484px;width:568px"></div>
<div class="abs send">
  <svg width="12" height="12" viewBox="0 0 12 12"><path d="M12 0L0 5l4.5 1.5L6 12z" fill="#fff"/></svg>
</div>

<!-- map -->
<div class="abs map" role="img" aria-label="Street map showing the shop location"></div>

<!-- footer -->
<footer class="abs footer"></footer>
<div class="abs logo" style="left:88px;top:960px;font-size:20px;color:#fff">TOLVENA CARE <span class="dot" style="background:#fff;width:9px;height:9px"></span></div>
<div class="abs ftext" style="left:88px;top:1009px">
  <svg width="9" height="12" viewBox="0 0 10 13"><path d="M5 0a5 5 0 0 0-5 5c0 3.5 5 8 5 8s5-4.5 5-8a5 5 0 0 0-5-5z" fill="#e8202a"/><circle cx="5" cy="5" r="1.8" fill="#252637"/></svg>
  &nbsp;Address : 52 ellery st, Parkes.
</div>
<div class="abs ftext" style="left:88px;top:1037px">
  <svg width="9" height="9" viewBox="0 0 10 10"><path d="M2 0l2 2.5-1.2 1.3c.8 1.6 1.8 2.6 3.4 3.4L7.5 6 10 8l-1.5 2C4 9.5.5 6 0 1.5z" fill="#e8202a"/></svg>
  &nbsp;Phone : 40517328
</div>
<div class="abs ftext" style="left:88px;top:1064px">
  <svg width="10" height="7" viewBox="0 0 11 8"><rect width="11" height="8" fill="#e8202a"/><path d="M0 0l5.5 4.5L11 0" fill="none" stroke="#252637"/></svg>
  &nbsp;Email : www.tolvenacare.com
</div>

<h3 class="abs fh" style="left:381px;top:954px">Quick Links</h3>
<div class="abs frule" style="left:382px;top:985px"></div>
<div class="abs ftext" style="left:381px;top:1007px"><span class="chev">›</span> Home</div>
<div class="abs ftext" style="left:381px;top:1033px"><span class="chev">›</span> About Us</div>
<div class="abs ftext" style="left:381px;top:1059px"><span class="chev">›</span> Services</div>
<div class="abs ftext" style="left:381px;top:1085px"><span class="chev">›</span> Products</div>
<div class="abs ftext" style="left:503px;top:1007px"><span class="chev">›</span> Gallery</div>
<div class="abs ftext" style="left:503px;top:1033px"><span class="chev">›</span> Blog</div>
<div class="abs ftext" style="left:503px;top:1059px"><span class="chev">›</span> Contact Us</div>

<h3 class="abs fh" style="left:682px;top:954px">Follow us</h3>
<div class="abs frule" style="left:683px;top:985px"></div>
<div class="abs ftext" style="left:682px;top:1007px;color:var(--red)"><span class="fdot" style="background:var(--red)"></span> Friendbook</div>
<div class="abs ftext" style="left:682px;top:1033px"><span class="fdot"></span> Chirper</div>
<div class="abs ftext" style="left:682px;top:1059px"><span class="fdot"></span> Circles +</div>
<div class="abs ftext" style="left:682px;top:1085px"><span class="fdot"></span> Workednet</div>

<h3 class="abs fh" style="left:865px;top:954px">Newsletter signup</h3>
<div class="abs frule" style="left:866px;top:985px"></div>
<div class="abs ftext" style="left:866px;top:1007px">Subscribe to our newsletter for updates.</div>
<div class="abs ftext" style="left:866px;top:1044px;font-size:11.5px">
  <svg width="10" height="7" viewBox="0 0 11 8"><rect width="11" height="8" fill="#fff"/><path d="M0 0l5.5 4.5L11 0" fill="none" stroke="#252637"/></svg>
  Enter email address...
</div>
<div class="abs" style="left:866px;top:1067px;width:224px;height:1px;background:#3c3d4e"></div>
<div class="abs submit">SUBMIT</div>

<div class="abs ftext" style="left:88px;top:1169px">© 2017 All rights reserved</div>
<div class="abs ftext" style="right:87px;top:1169px">Privacy Policy Terms &amp; Conditions</div>
<div class="abs totop">
  <svg width="10" height="6" viewBox="0 0 10 6"><path d="M1 5l4-4 4 4" fill="none" stroke="#222" stroke-width="1.5"/></svg>
</div>

</body>
</html>
```